Create Website for new company called "Verdant Lodge 17"

Verdant Lodge 17 is a new business situated in Southwestern Colorado. We are creating a business that will rent out spaces where clients can grow their own marijuana. Picture a large green house with partitioned spaces that are secured by a lock. Best way to envision this would be to think of a storage business that rents out storage rooms. The difference is that we will be having the units inside a green house ( for growing purposes) Picture a small area that is secured by locks, Picture an area that has the ability to provide state of the art security, cameras etc. We want to focus our efforts on professionals, blue collar workers and end users of marijuana. Our emphasis is in the area of assisting those whom wish to grow their own plants. We want to provide them a safe facility in which to do that. . Keep in mind that we also build custom grow rooms at clients homes and provide a grow pod (lease these) where a small grow unit will be delivered and picked up from our clients whom want to lease a unit for a short amount of time. We have a business card ( just designed) and will send that information to those whom express an interests in this project. We want to be able to sign people up for our services by entering an agreement and signing the agreement while on the internet. We want to provide our services to those whom consume recreational and medical marijuana. This site will need to gather information I.e email addresses so that we can followup with offers. This is a tremendous opportunity for the right designer. We will be creating many more websites as other states come on line and make marijuana legal to consume. Use the business card model for a point of reference of how we envision the concept. That is a business card we just recently printed. The hands and the plant is our logo so far. Open to suggestions. There will be three levels of service. Bronze, Silver, Gold or Platinum. We will also have a retail biz down the road but not at the present time.

Target Market(s)

Ages 21-60

Industry/Entity Type

Medical

Logo Text

Verdant Lodge 17.

Number of Pages Required

5+ page

Requirements
Must have
• Clean appearance not to busy , easily navigable from link to link, page to page. Must have ability down the road to enter into a contractual agreement via the website. Must use our provided logo and example of that is on our business card that will be uploaded here shortly. We would like to have the colors that are on the business card however if you have suggestions or color schemes that you want us to consider that is okay.
Nice to have
• Nice to have a animation of seed to weed and how clients can save a tremendous amount of money growing their own cannabis. Nice to have testimonial page or feedback page. Have a membership component to website,
Should not have
• No flashing lights, etc. Not to busy in terms of animations.

```html
<!DOCTYPE html>
<html lang="en">
<head>
<meta charset="utf-8">
<title>Verdant Lodge 17</title>
<link href="https://fonts.googleapis.com/css2?family=Oswald:wght@400;500&family=Titillium+Web:wght@400;600&family=Open+Sans:wght@400;600&display=swap" rel="stylesheet">
<style>
:root{
  --green:#1a8a4a;
  --green-head:#1f7d45;
  --orange:#c8782e;
  --orange-dark:#a95f1f;
  --slate:#2f3a3a;
  --ink:#333;
  --muted:#555;
  --black:#0a0a0a;
  --white:#fff;
  --red:#e0504a;
}
*{margin:0;padding:0;box-sizing:border-box}
html,body{width:688px;height:1200px;overflow:hidden;background:var(--white)}
body{position:relative;font-family:'Open Sans',sans-serif;color:var(--ink)}
.abs{position:absolute}
.brand{left:65px;top:30px;display:flex;align-items:center;gap:7px;font-family:'Oswald',sans-serif;font-weight:500;font-size:20px;color:var(--slate);letter-spacing:.3px}
.brand-dot{width:12px;height:12px;border-radius:50%;background:var(--green)}
.nav{left:296px;top:18px;width:392px;height:44px;background:var(--orange);display:flex;font-family:'Oswald',sans-serif;font-size:10.5px;color:var(--white)}
.nav a{color:inherit;text-decoration:none;display:flex;align-items:center;justify-content:center;height:100%}
.nav .active{background:var(--slate);width:62px}
.nav .item{padding:0 18px}
.hero{left:0;top:83px;width:688px;height:314px;background:linear-gradient(180deg,#b9bfbf 0%,#7f9a6a 40%,#3f6a2a 75%,#2d4e1f 100%)}
.hero-caption{left:66px;top:198px;width:254px;height:75px;background:var(--green);color:var(--white);font-family:'Oswald',sans-serif;font-size:18px;line-height:21px;padding:15px 11px}
.arrow{top:229px}
.dots{left:327px;top:378px;display:flex;gap:4px}
.dots span{width:5px;height:5px;border-radius:50%;background:var(--white)}
.dots span:first-child{background:var(--orange)}
h2{font-family:'Titillium Web',sans-serif;font-weight:600;color:var(--green-head)}
.welcome-title{left:65px;top:406px;font-size:17px}
.welcome-text{left:65px;top:430px;width:345px;font-size:6.2px;line-height:13.7px;color:var(--muted)}
.welcome-photo{left:420px;top:411px;width:201px;height:131px;background:radial-gradient(circle at 55% 50%,#8fd44a,#3e9a1e 70%,#2d7a15)}
.services-title{left:65px;top:566px;font-size:17px}
.service{top:601px;width:172px}
.service .photo{height:101px}
.service h3{font-family:'Titillium Web',sans-serif;font-weight:400;font-size:12px;color:#222;margin-top:7px}
.service p{font-size:6.6px;line-height:12px;color:var(--muted);margin-top:2px}
.btn{display:inline-block;margin-top:9px;width:72px;height:21px;line-height:21px;text-align:center;font-family:'Oswald',sans-serif;font-size:7px;color:var(--white);background:linear-gradient(180deg,var(--orange),var(--orange-dark));border-radius:2px}
.blog-title{left:65px;top:836px;font-size:12.5px}
.tweet-title{left:434px;top:839px;width:200px;text-align:center;font-size:12.5px}
.post{top:867px;width:185px}
.post .photo{height:88px}
.post .meta{font-size:6.2px;color:var(--muted);margin-top:10px}
.post .title{font-size:6.8px;font-weight:600;color:#111;margin-top:5px}
.tweet{left:454px;top:874px;width:160px;text-align:center;font-size:9px;line-height:12.6px;color:#444}
.tweet .rule{width:38px;height:2px;background:var(--red);margin:10px auto 10px}
.tweet .ago{font-size:6.3px;color:var(--muted)}
.band{left:0;top:1014px;width:688px;height:119px;background:var(--green);color:var(--white);font-family:'Titillium Web',sans-serif}
.band .motto{position:absolute;top:13px;width:100%;text-align:center;font-size:13px;font-weight:600}
.contact{position:absolute;top:50px;font-size:13.5px;line-height:21px}
.footer{left:0;top:1133px;width:688px;height:67px;background:var(--black);color:var(--white)}
.footer .links{position:absolute;left:66px;top:17px;font-size:7px}
.footer .copy{position:absolute;left:66px;top:34px;font-size:7px}
.social{position:absolute;top:22px;width:18px;height:18px}
</style>
</head>
<body>
<div class="abs brand"><span class="brand-dot"></span>VERDANT LODGE 17</div>
<nav class="abs nav">
  <a class="active">Home</a><a class="item">About Us</a><a class="item">Services</a><a class="item">Blog</a><a class="item">Contact Us</a>
</nav>

<div class="abs hero" role="img" aria-label="Photo of tall cannabis plants growing under a pale sky"></div>
<svg class="abs arrow" style="left:26px" width="12" height="18" viewBox="0 0 12 18"><path d="M10 1 2 9l8 8" fill="none" stroke="#c8782e" stroke-width="3"/></svg>
<svg class="abs arrow" style="left:650px" width="12" height="18" viewBox="0 0 12 18"><path d="M2 1l8 8-8 8" fill="none" stroke="#c8782e" stroke-width="3"/></svg>
<div class="abs hero-caption">Rent out spaces where clients can grow their own marijuana</div>
<div class="abs dots"><span></span><span></span><span></span></div>

<h2 class="abs welcome-title">Welcome To Our Comapny</h2>
<p class="abs welcome-text">Lorem ipsum dolor sit amet, consectetuer adipiscing elit, sed diam nonummy nibh euismod tincidunt ut laoreet dolore magna aliquam erat volutpat. Ut wisi enim ad minim veniam, quis nostrud exerci tation ullamcorper suscipit lobortis nisl ut aliquip ex ea commodo consequat. Lorem ipsum dolor sit amet, consectetuer adipiscing elit, sed diam nonummy nibh euismod tincidunt ut laoreet dolore magna aliquam erat volutpat. Ut wisi enim ad minim veniam, quis nostrud exerci tation ullamcorper suscipit lobortis nisl ut aliquip ex ea commodo consequat.Lorem ipsum dolor sit amet, consectetuer adipiscing elit, sed diam nonummy nibh euismod tincidunt ut laoreet dolore magna aliquam erat volutpat. Ut wisi enim ad minim veniam, quis nostrud exerci tation ullamcorper suscipit lobortis nisl ut aliquip ex ea commodo consequat.</p>
<div class="abs welcome-photo" role="img" aria-label="Close-up photo of bright green cannabis leaves"></div>

<h2 class="abs services-title">Our Services</h2>
<div class="abs service" style="left:65px">
  <div class="photo" role="img" aria-label="Photo of a cannabis plant inside a wooden greenhouse" style="background:linear-gradient(180deg,#b88a5a 0%,#6fa050 35%,#2f7a2a 100%)"></div>
  <h3>Consectetuer adipiscing elit</h3>
  <p>Lorem ipsum dolor sit amet, consectetuer adipiscing elit, sed diam nonummy nibh euismod tincidunt ut laoreet dolore magna aliquam erat volutpat.</p>
  <span class="btn">READ MORE</span>
</div>
<div class="abs service" style="left:261px">
  <div class="photo" role="img" aria-label="Photo of cannabis plants in a greenhouse with wooden beams" style="background:linear-gradient(180deg,#a88055 0%,#5e9a3e 40%,#2a6f22 100%)"></div>
  <h3>Consectetuer adipiscing elit</h3>
  <p>Lorem ipsum dolor sit amet, consectetuer adipiscing elit, sed diam nonummy nibh euismod tincidunt ut laoreet dolore magna aliquam erat volutpat. Read more.....</p>
  <span class="btn">READ MORE</span>
</div>
<div class="abs service" style="left:450px">
  <div class="photo" role="img" aria-label="Photo of a young cannabis plant against a soft green background" style="background:radial-gradient(circle at 50% 55%,#6fae2e,#a6cc4a 60%,#8fbd3c)"></div>
  <h3>Consectetuer adipiscing elit</h3>
  <p>Lorem ipsum dolor sit amet, consectetuer adipiscing elit, sed diam nonummy nibh euismod tincidunt ut laoreet dolore magna aliquam erat volutpat. Read more.....</p>
  <span class="btn">READ MORE</span>
</div>

<h2 class="abs blog-title">Latest Blog</h2>
<div class="abs post" style="left:65px">
  <div class="photo" role="img" aria-label="Photo of a large wooden lodge-style house" style="background:linear-gradient(180deg,#9ab8d8 0%,#8a6a4a 50%,#5a4a3a 100%)"></div>
  <div class="meta">Aug 9, 2013 &nbsp;3 comments</div>
  <div class="title">Lorem ipsum dolor sit amet</div>
</div>
<div class="abs post" style="left:260px">
  <div class="photo" role="img" aria-label="Photo of a white two-storey house with front steps" style="background:linear-gradient(180deg,#8aa8cc 0%,#e8e6e2 45%,#8a8a86 100%)"></div>
  <div class="meta">Aug 9, 2013 &nbsp;3 comments</div>
  <div class="title">Lorem ipsum dolor sit amet</div>
</div>

<h2 class="abs tweet-title">Latest Tweet</h2>
<div class="abs tweet">
  <svg width="16" height="13" viewBox="0 0 16 13"><path d="M1 2h14v8H6l-3 3v-3H1z" fill="#666"/></svg>
  <div style="margin-top:3px">@verdantlodge<br>Are you ready to sell some burgers? Our Grow Pod plan is now equipped with online sign-up form!</div>
  <div class="rule"></div>
  <div class="ago">about 12 days ago</div>
</div>

<section class="abs band">
  <div class="motto">“supporting the care &amp; cultivation of cannabis”</div>
  <div class="contact" style="left:65px">Evan Marlow<br>cell 555.201.4417</div>
  <div class="contact" style="left:261px;width:170px;text-align:center">Owen Marlow<br>Owen@VerdantLodge17.com</div>
  <div class="contact" style="right:66px;text-align:right">Dale Whitcomb<br>cell 555.309.2261</div>
</section>

<footer class="abs footer">
  <div class="links">Home | About Us | Services | Blog | Contact Us</div>
  <div class="copy">© 2014 Verdant Lodge 17 &nbsp;All Rights Reserved</div>
  <span class="social" style="left:518px;background:#3b5998"></span>
  <span class="social" style="left:547px;background:#2a9fd6"></span>
  <span class="social" style="left:577px;background:#cfcfcf"></span>
  <span class="social" style="left:606px;background:#1f7bb6"></span>
</footer>
</body>
</html>
```